Modern Lawfirm Business Card Design

We're looking for a business card to incorporate the newly created logo we had made.

Ideally looking for a law firm business card demonstrating, modern, minimalist, strong/bold design.

I'm open to any design honestly, but nothing "flashy".

Target Market(s)

Immigration law, family immigration, humanitarian, general legal

Industry/Entity Type

Law Firm

Contact Information for Business Card

Please use dummy information, name, street address, city, state, phone number, email, website.

Font styles to use
Serif
Sans Serif

Requirements
Must have
• Please use dummy information, name, street address, city, state, phone number, email, website.

```html
<!DOCTYPE html>
<html lang="en">
<head>
<meta charset="utf-8">
<title>Valdora Immigration Law – Business Card</title>
<link rel="stylesheet" href="https://fonts.googleapis.com/css2?family=Cinzel:wght@500&family=Montserrat:wght@800&family=Open+Sans:wght@400;600&display=swap">
<style>
  :root {
    --page-bg: #e4e5e7;
    --blue-deep: #1d5c9e;
    --blue-mid: #1470b8;
    --blue-light: #1a7cc6;
    --band: #2e86cf;
    --white: #ffffff;
    --ink: #111418;
    --link-blue: #1c5e9f;
    --shadow: rgba(20, 30, 45, 0.18);
  }
  * { box-sizing: border-box; margin: 0; padding: 0; }
  html, body {
    width: 1000px; height: 1200px; overflow: hidden;
    background: var(--page-bg);
  }
  .sheet {
    position: relative; width: 1000px; height: 1200px;
    display: flex; flex-direction: column; align-items: center; justify-content: center;
    gap: 70px;
  }
  .card {
    position: relative; width: 700px; height: 400px; overflow: hidden;
    box-shadow: 0 6px 22px var(--shadow);
  }
  .blue-field {
    position: absolute; top: 0; bottom: 0;
    background: linear-gradient(160deg, var(--blue-deep) 0%, var(--blue-mid) 55%, var(--blue-light) 100%);
  }
  .blue-field::before, .blue-field::after {
    content: ""; position: absolute; left: 0; right: 0; height: 10px; background: var(--band);
  }
  .blue-field::before { top: 8px; }
  .blue-field::after { bottom: 8px; }

  .wordmark {
    position: absolute; color: var(--white);
    font-family: "Cinzel", serif; font-weight: 500; text-align: center;
    display: flex; flex-direction: column; align-items: center; line-height: 1;
  }
  .wordmark .name { letter-spacing: 0.02em; }
  .wordmark .practice { letter-spacing: 0.55em; margin-top: 10px; padding-left: 0.55em; }

  /* front */
  .card-front .blue-field { left: 0; right: 0; }
  .card-front .wordmark { left: 0; right: 0; top: 50%; transform: translateY(-50%); }
  .card-front .wordmark .name { font-size: 82px; }
  .card-front .wordmark .practice { font-size: 17px; }

  /* back */
  .card-back { background: var(--white); }
  .card-back .blue-field { left: 50%; right: 0; }
  .card-back .wordmark { left: 50%; right: 0; top: 50%; transform: translateY(-50%); }
  .card-back .wordmark .name { font-size: 46px; }
  .card-back .wordmark .practice { font-size: 10px; margin-top: 7px; }

  .contact-panel { position: absolute; left: 48px; top: 112px; width: 290px; }
  .person-name {
    font-family: "Montserrat", sans-serif; font-weight: 800; font-size: 26px;
    color: var(--ink); letter-spacing: 0.01em;
  }
  .person-role {
    font-family: "Open Sans", sans-serif; font-weight: 600; font-size: 8px;
    color: var(--ink); letter-spacing: 0.06em; margin-top: 2px;
  }
  .contact-list { list-style: none; margin-top: 36px; }
  .contact-list li {
    display: flex; align-items: flex-start; gap: 14px; margin-bottom: 12px;
    font-family: "Open Sans", sans-serif; font-size: 17px; color: var(--link-blue); line-height: 1.15;
  }
  .contact-list svg { flex: 0 0 18px; width: 18px; height: 18px; margin-top: 1px; }
</style>
</head>
<body>
<main class="sheet">

  <section class="card card-front" aria-label="Business card front">
    <div class="blue-field"></div>
    <div class="wordmark">
      <span class="name">VALDORA</span>
      <span class="practice">IMMIGRATION LAW</span>
    </div>
  </section>

  <section class="card card-back" aria-label="Business card back">
    <div class="contact-panel">
      <h1 class="person-name">NAME IS HERE</h1>
      <p class="person-role">DESIGNATION</p>
      <ul class="contact-list">
        <li>
          <svg viewBox="0 0 18 18" aria-hidden="true"><circle cx="9" cy="9" r="9" fill="var(--link-blue)"/><path d="M6 5l2 0 1 2.5-1.3 1a5 5 0 0 0 2.3 2.3l1-1.3L13.5 10.5V12.5a1 1 0 0 1-1 1A7.5 7.5 0 0 1 5 6a1 1 0 0 1 1-1z" fill="#fff"/></svg>
          <span>123 425 654</span>
        </li>
        <li>
          <svg viewBox="0 0 18 18" aria-hidden="true"><circle cx="9" cy="9" r="9" fill="var(--link-blue)"/><circle cx="9" cy="9" r="4.5" fill="none" stroke="#fff" stroke-width="1.2"/><path d="M4.5 9h9M9 4.5c-2 2.5-2 6.5 0 9M9 4.5c2 2.5 2 6.5 0 9" fill="none" stroke="#fff" stroke-width="1"/></svg>
          <span>www.xxx-xxx-xxx.com</span>
        </li>
        <li>
          <svg viewBox="0 0 18 18" aria-hidden="true"><circle cx="9" cy="9" r="9" fill="var(--link-blue)"/><rect x="4.5" y="6" width="9" height="6.5" fill="none" stroke="#fff" stroke-width="1.2"/><path d="M4.5 6l4.5 3.8L13.5 6" fill="none" stroke="#fff" stroke-width="1.2"/></svg>
          <span>xxx-xxx-xxx@gmail.com</span>
        </li>
        <li>
          <svg viewBox="0 0 18 18" aria-hidden="true"><circle cx="9" cy="9" r="9" fill="var(--link-blue)"/><path d="M9 4a3.3 3.3 0 0 1 3.3 3.3C12.3 10 9 14 9 14S5.7 10 5.7 7.3A3.3 3.3 0 0 1 9 4z" fill="#fff"/><circle cx="9" cy="7.3" r="1.2" fill="var(--link-blue)"/></svg>
          <span>address line 1<br>address line 2</span>
        </li>
      </ul>
    </div>
    <div class="blue-field"></div>
    <div class="wordmark">
      <span class="name">VALDORA</span>
      <span class="practice">IMMIGRATION LAW</span>
    </div>
  </section>

</main>
</body>
</html>
```